Vehicle Signage for Plumbing Fleet of Vans

We are a plumbing service in Perth, Western Australia who requires vehicle signage for our fleet of plumbing vans.

Our business name is Larkmoor Plumbing. I have attached the various versions of our logo in .eps, .pdf and .ai format. I have also attached images of the vans from side and rear profile.

I would prefer the signage not to include images of pipes, water or plumbing paraphernalia. We encompass all areas of plumbing from new build to renovations to maintenance.

What we do need on the vans are the following details;

Logo
Larkmoor Plumbing
larkmoorplumbing.com.au

I would like the graphics to cover the back of the van and go about 3/4 of the way along the side of the van. They should modern and reflect a forward thinking company.

Target Market(s)

builders, renovators, home owners

Industry/Entity Type

Business

Font styles to use
Sans Serif

Requirements
Must have
• our logo
• our website
• our name
• our brand's colour - charcoal / grey
Should not have
• images of plumbing paraphernalia, pipes or water etc.

```html
<!DOCTYPE html>
<html lang="en">
<head>
<meta charset="utf-8">
<title>Larkmoor Plumbing – Van Signage</title>
<link rel="stylesheet" href="https://fonts.googleapis.com/css2?family=Open+Sans:wght@400;600;700&display=swap">
<style>
  :root {
    --backdrop: #f2f2f2;
    --van-white: #f4f4f2;
    --charcoal: #3a3a3a;
    --charcoal-deep: #2b2b2b;
    --graphite-mid: #6e6e6e;
    --emblem-fill: #4a4a4a;
    --glass: #2e3236;
    --trim: #1e1e1e;
    --hub: #b9bcbf;
    --ink: #4a4a4a;
    --wrap-text: #ffffff;
  }
  html, body {
    margin: 0;
    padding: 0;
    width: 1200px;
    height: 800px;
    overflow: hidden;
    background: var(--backdrop);
    font-family: "Open Sans", sans-serif;
  }
  .canvas {
    position: relative;
    width: 1200px;
    height: 800px;
  }
  .van,
  .emblem-area {
    position: absolute;
    left: 0;
    top: 0;
    width: 1200px;
    height: 800px;
  }
  .wrap-title {
    position: absolute;
    left: 410px;
    top: 220px;
    margin: 0;
    color: var(--wrap-text);
    font-weight: 400;
    font-size: 29px;
    line-height: 33px;
    letter-spacing: 6.6px;
    text-transform: uppercase;
  }
  .door-signage {
    position: absolute;
    left: 756px;
    top: 346px;
    color: var(--ink);
  }
  .door-brand {
    display: flex;
    align-items: center;
    gap: 8px;
  }
  .door-brand-dot {
    width: 28px;
    height: 28px;
    border-radius: 50%;
    background: var(--ink);
  }
  .door-brand-name {
    font-weight: 600;
    font-size: 15px;
    line-height: 16px;
    letter-spacing: 1px;
    text-transform: uppercase;
    width: 110px;
  }
  .door-web {
    font-size: 12px;
    margin-top: 3px;
  }
  .door-phone {
    margin-left: -58px;
    margin-top: 2px;
    font-weight: 700;
    font-size: 27px;
    letter-spacing: 1.5px;
  }
</style>
</head>
<body>
<main class="canvas">
  <svg class="van" viewBox="0 0 1200 800" aria-hidden="true">
    <defs>
      <linearGradient id="wrap-fade" x1="0" y1="0" x2="1" y2="0">
        <stop offset="0" stop-color="var(--charcoal-deep)"/>
        <stop offset="0.45" stop-color="var(--charcoal)"/>
        <stop offset="0.75" stop-color="var(--graphite-mid)"/>
        <stop offset="1" stop-color="var(--van-white)"/>
      </linearGradient>
    </defs>
    <path class="van-body" d="M95 200 Q100 168 140 166 L660 166 Q700 168 730 180 L860 220 Q960 280 1060 340 Q1100 370 1100 420 L1100 500 Q1098 520 1080 525 L110 525 Q85 520 82 500 L82 300 Z" fill="var(--van-white)"/>
    <path class="wrap-panel" d="M95 200 Q100 168 140 166 L670 166 L670 530 L110 530 Q85 520 82 500 L82 300 Z" fill="url(#wrap-fade)"/>
    <path class="cab-window" d="M690 195 L850 200 Q900 240 945 330 L690 330 Z" fill="var(--glass)"/>
    <line x1="670" y1="180" x2="670" y2="525" stroke="#9a9a9a" stroke-width="2"/>
    <line x1="905" y1="330" x2="880" y2="525" stroke="#bcbcbc" stroke-width="2"/>
    <rect x="617" y="343" width="128" height="36" rx="6" fill="var(--trim)"/>
    <rect x="360" y="462" width="540" height="8" fill="var(--trim)" opacity="0.7"/>
    <path d="M78 470 L78 520 Q80 530 100 532 L190 532 L190 470 Z" fill="var(--trim)"/>
    <path d="M1040 480 L1100 480 L1100 515 Q1095 532 1070 534 L1040 534 Z" fill="var(--trim)"/>
    <rect x="84" y="330" width="22" height="60" rx="6" fill="#c83a3a"/>
    <circle cx="280" cy="528" r="72" fill="var(--trim)"/>
    <circle cx="280" cy="528" r="44" fill="var(--hub)"/>
    <circle cx="975" cy="520" r="70" fill="var(--trim)"/>
    <circle cx="975" cy="520" r="43" fill="var(--hub)"/>
  </svg>

  <svg class="emblem-area" viewBox="0 0 1200 800" role="img" aria-label="Large brand emblem area on the rear side panel">
    <circle cx="255" cy="318" r="135" fill="var(--emblem-fill)" stroke="var(--wrap-text)" stroke-width="6"/>
  </svg>

  <h1 class="wrap-title">Larkmoor<br>Plumbing</h1>

  <section class="door-signage">
    <div class="door-brand">
      <span class="door-brand-dot"></span>
      <span class="door-brand-name">Larkmoor Plumbing</span>
    </div>
    <div class="door-web">larkmoorplumbing.com.au</div>
    <div class="door-phone">0400 555 018</div>
  </section>
</main>
</body>
</html>
```